DRM Letterhead Design Project

Design a new company letterhead utilizing our new logo and color scheme. Interested in professional letterhead and matching 2nd sheet versions.
Updates

I have uploaded windows format files now.  Originally only uploaded MAC file format.  Good luck!

Target Market(s)

Industry Executives, construction managers, well educated and discriminate personnel. Project needs to leave an impression and have impact but not be cluttered, busy or too in your face.

Industry/Entity Type

It Company

Requirements
Must have
• Clean, crisp look, true to new logo and color scheme, professional image. Should include spaces for company web address, address info and phone & fax numbers

```html
<!DOCTYPE html>
<html lang="en">
<head>
<meta charset="utf-8">
<title>Beacon Guard Stationery</title>
<link href="https://fonts.googleapis.com/css2?family=Arimo:wght@400;700&display=swap" rel="stylesheet">
<style>
  :root {
    --backdrop: #e0e0df;
    --brand-orange: #d3791f;
    --brand-grey: #4d4d4f;
    --paper: #ffffff;
    --watermark: #f3f3f3;
    --ink: #2b2b2b;
  }
  * { margin: 0; padding: 0; box-sizing: border-box; }
  html, body { width: 1200px; height: 845px; overflow: hidden; }
  body {
    position: relative;
    background: var(--backdrop);
    font-family: "Arimo", Arial, sans-serif;
    color: var(--ink);
  }
  .cover-sheet {
    position: absolute; left: 191px; top: 131px;
    width: 389px; height: 552px;
    background: var(--brand-orange);
  }
  .cover-mark {
    position: absolute; left: 158px; top: 196px;
    width: 72px; height: 72px; border-radius: 50%;
    background: var(--brand-grey);
  }
  .cover-name {
    position: absolute; left: 0; right: 0; top: 297px;
    text-align: center; color: #fff;
    font-weight: 700; font-size: 29px; letter-spacing: 1px;
  }
  .letter-sheet {
    position: absolute; left: 636px; top: 133px;
    width: 389px; height: 550px;
    background: var(--paper); overflow: hidden;
  }
  .letter-watermark { position: absolute; left: 0; top: 0; }
  .letter-header { position: absolute; left: 0; top: 0; width: 389px; height: 62px; }
  .header-brand {
    position: absolute; left: 26px; top: 14px;
    display: flex; align-items: center; gap: 9px;
  }
  .header-brand-dot { width: 32px; height: 32px; border-radius: 50%; background: var(--brand-grey); }
  .header-brand-name { color: #fff; font-weight: 700; font-size: 13px; letter-spacing: 0.5px; }
  .header-contact {
    position: absolute; right: 8px; top: 11px;
    color: #fff; font-size: 4.6px; line-height: 5.6px; text-align: right;
  }
  .contact-row { display: flex; justify-content: flex-end; align-items: flex-start; gap: 6px; margin-bottom: 3px; }
  .contact-row svg { flex: none; margin-top: 1px; }
  .letter-body { position: absolute; left: 30px; top: 125px; width: 330px; font-size: 6.3px; line-height: 8px; }
  .letter-title { font-weight: 700; margin-bottom: 8px; }
  .letter-body p.paragraph { text-align: justify; margin-bottom: 8px; }
  .letter-signoff { margin-top: 14px; }
  .footer-line { position: absolute; left: 0; bottom: 0; width: 389px; height: 3px; }
</style>
</head>
<body>
  <section class="cover-sheet">
    <div class="cover-mark"></div>
    <div class="cover-name">BEACON GUARD</div>
  </section>

  <section class="letter-sheet">
    <svg class="letter-watermark" width="389" height="550" aria-hidden="true">
      <circle cx="195" cy="290" r="235" fill="var(--watermark)"/>
    </svg>

    <svg class="letter-header" width="389" height="62" aria-hidden="true">
      <rect width="389" height="62" fill="var(--brand-orange)"/>
      <polygon points="280,0 389,0 389,62 224,62" fill="var(--brand-grey)"/>
    </svg>
    <div class="header-brand">
      <div class="header-brand-dot"></div>
      <div class="header-brand-name">BEACON GUARD</div>
    </div>
    <div class="header-contact">
      <div class="contact-row">
        <div>Your office or<br>home address</div>
        <svg width="5" height="6" viewBox="0 0 10 12"><path d="M5 0a4 4 0 0 1 4 4c0 3-4 8-4 8S1 7 1 4a4 4 0 0 1 4-4z" fill="#fff"/></svg>
      </div>
      <div class="contact-row">
        <div>+000 1234 567<br>+000 1234 567</div>
        <svg width="6" height="5" viewBox="0 0 12 10"><path d="M1 3c3-3 7-3 10 0l-2 2-2-1V3H5v1L3 5z M3 6h6v4H3z" fill="#fff"/></svg>
      </div>
      <div class="contact-row">
        <div>mail@beaconguard.com<br>www.beaconguard.com</div>
        <svg width="6" height="5" viewBox="0 0 12 10"><rect x="0" y="1" width="12" height="8" fill="#fff"/></svg>
      </div>
    </div>

    <div class="letter-body">
      <p class="letter-title">Lorem ipsum</p>
      <p class="paragraph">Lorem ipsum dolor, consectetuer adipiscing elit, sed diam nonummy nibh euismod tincidunt ut laoreet dolore magna aliquam erat volutpat. Ut wisi enim ad minim veniam, quis nostrud exerci tation ullamcorper suscipit lobortis nisl ut aliquip ex ea commodo consequat. Duis autem vel eum iriure dolor in hendrerit in vulputate velit esse molestie consequat, vel illum dolore eu feugiat nulla facilisis minim</p>
      <p class="paragraph">Lorem ipsum dolor, consectetuer adipiscing elit, sed diam nonummy nibh euismod tincidunt ut laoreet dolore magna aliquam erat volutpat. Ut wisi enim ad minim veniam, quis nostrud exerci tation ullamcorper suscipit lobortis nisl ut aliquip ex ea commodo consequat. Duis autem vel eum iriure dolor in hendrerit in vulputate velit esse molestie consequat, vel illum dolore eu feugiat nulla facilisis minim</p>
      <p class="paragraph">Lorem ipsum dolor, consectetuer adipiscing elit, sed diam nonummy nibh euismod tincidunt ut laoreet dolore magna aliquam erat volutpat. Ut wisi enim ad minim veniam, quis nostrud exerci tation ullamcorper suscipit lobortis nisl ut aliquip ex ea commodo consequat. Duis autem vel eum iriure dolor in hendrerit in vulputate velit esse molestie consequat, vel illum dolore eu feugiat nulla facilisis minim</p>
      <p class="paragraph">Lorem ipsum dolor, consectetuer adipiscing elit, sed diam nonummy nibh euismod tincidunt ut laoreet dolore magna aliquam erat volutpat. Ut wisi enim ad minim veniam, quis nostrud exerci tation ullamcorper suscipit lobortis nisl ut aliquip ex ea commodo consequat. Duis autem vel eum iriure dolor in hendrerit in vulputate velit esse molestie consequat, vel illum dolore eu feugiat nulla facilisis minim</p>
      <p class="paragraph">Lorem ipsum dolor, consectetuer adipiscing elit, sed diam nonummy nibh euismod tincidunt ut laoreet dolore magna aliquam erat volutpat. Ut wisi enim ad minim veniam, quis nostrud exerci tation ullamcorper suscipit lobortis nisl ut aliquip ex ea commodo consequat. Duis autem vel eum iriure dolor in hendrerit in vulputate velit esse molestie consequat, vel illum dolore eu feugiat nulla facilisis minim</p>
      <p class="paragraph">Lorem ipsum dolor, consectetuer adipiscing elit, sed diam nonummy nibh euismod tincidunt ut laoreet dolore magna aliquam erat volutpat. Ut wisi enim ad minim veniam, quis nostrud exerci tation ullamcorper suscipit lobortis nisl ut aliquip ex ea commodo consequat. Duis autem vel eum iriure dolor in hendrerit in vulputate velit esse molestie consequat, vel illum dolore eu feugiat nulla facilisis minim</p>
      <p class="letter-signoff">Yours Sincerely,</p>
    </div>

    <svg class="footer-line" width="389" height="3" aria-hidden="true">
      <rect width="389" height="3" fill="var(--brand-orange)"/>
      <rect width="135" height="3" fill="var(--brand-grey)"/>
    </svg>
  </section>
</body>
</html>
```